Pharmacist turned chef in Key West Fl needs a logo design

I am looking for a professional looking business card that says who I am and what I do. For example Chef Dale Morrow, natural organic and health supportive cooking. Phone 305-617-4289 email dalemorrow@quillpost.example web www.thehearthremedy.example, Key West fl. The color or colors should have some green and other colors that look good together that stimulate appetite and give a clean healthy image. To help with a thought process, words like food as medicine, medicine is food, good nutrition is health but at the same time I do not want a lot of medical symbols that me it look clinical. Any questions please contact me.

```html
<!DOCTYPE html>
<html lang="en">
<head>
<meta charset="utf-8">
<title>The Hearth Remedy — Identity</title>
<link href="https://fonts.googleapis.com/css2?family=Arimo:wght@400;700&display=swap" rel="stylesheet">
<style>
  :root {
    --green: #5f9a0f;
    --green-dark: #3f6f00;
    --green-light: #8cbd1a;
    --ink: #444446;
    --ink-soft: #555558;
    --paper: #ffffff;
    --rule: #b9b9b9;
    --stage: #f4f4f4;
    --swoosh: #f3f3f3;
  }
  * { margin: 0; padding: 0; box-sizing: border-box; }
  html, body { width: 1200px; height: 900px; overflow: hidden; }
  body {
    position: relative;
    background: var(--stage);
    font-family: "Arimo", Arial, sans-serif;
    color: var(--ink);
  }

  /* Wordmark lockup */
  .lockup { position: absolute; display: flex; align-items: center; }
  .lockup__dot { border-radius: 50%; background: var(--green); flex: none; }
  .lockup__text { display: flex; flex-direction: column; align-items: stretch; }
  .lockup__name { font-weight: 400; line-height: 0.92; color: var(--ink); letter-spacing: -0.5px; white-space: nowrap; }
  .lockup__tagline {
    border-top: 1px solid var(--ink);
    color: var(--ink-soft);
    white-space: nowrap;
    font-weight: 400;
  }

  .lockup--primary { left: 440px; top: 216px; gap: 20px; }
  .lockup--primary .lockup__dot { width: 92px; height: 92px; }
  .lockup--primary .lockup__name { font-size: 38px; }
  .lockup--primary .lockup__tagline { font-size: 8.5px; margin-top: 5px; padding-top: 3px; }

  /* Cards */
  .card { position: absolute; top: 415px; width: 460px; height: 282px; overflow: hidden; }

  .card--front {
    left: 130px;
    background: radial-gradient(circle at 58% 32%, var(--green-light) 0%, var(--green) 38%, var(--green-dark) 100%);
  }
  .card--front .lockup { left: 60px; top: 104px; gap: 18px; }
  .card--front .lockup__dot { width: 88px; height: 88px; background: var(--paper); }
  .card--front .lockup__name { font-size: 36px; color: var(--paper); }
  .card--front .lockup__tagline { font-size: 8px; color: var(--paper); border-color: var(--paper); margin-top: 5px; padding-top: 3px; }

  .card--back { left: 624px; background: var(--paper); box-shadow: 0 1px 3px rgba(0,0,0,0.18); }
  .card--back .lockup { left: 28px; top: 108px; gap: 8px; }
  .card--back .lockup__dot { width: 48px; height: 48px; }
  .card--back .lockup__name { font-size: 18px; }
  .card--back .lockup__tagline { font-size: 4.2px; margin-top: 3px; padding-top: 2px; }

  .card__swoosh { position: absolute; left: 0; top: 0; width: 460px; height: 282px; }
  .card__divider { position: absolute; left: 211px; top: 45px; width: 1px; height: 190px; background: var(--rule); }
  .card__band { position: absolute; left: 0; bottom: 0; width: 100%; height: 17px; background: var(--green); }

  .contact { position: absolute; right: 17px; text-align: right; color: var(--ink-soft); font-weight: 400; }
  .contact__heading { top: 46px; font-size: 46px; color: var(--ink); line-height: 1; }
  .contact__role { top: 110px; font-size: 13px; line-height: 15px; }
  .contact__details { top: 182px; font-size: 13px; line-height: 15px; }
</style>
</head>
<body>

  <div class="lockup lockup--primary">
    <span class="lockup__dot"></span>
    <div class="lockup__text">
      <span class="lockup__name">The Hearth<br>Remedy</span>
      <span class="lockup__tagline">wholesome food choices for lasting everyday wellness</span>
    </div>
  </div>

  <section class="card card--front">
    <div class="lockup">
      <span class="lockup__dot"></span>
      <div class="lockup__text">
        <span class="lockup__name">The Hearth<br>Remedy</span>
        <span class="lockup__tagline">wholesome food choices for lasting everyday wellness</span>
      </div>
    </div>
  </section>

  <section class="card card--back">
    <svg class="card__swoosh" viewBox="0 0 460 282" aria-hidden="true">
      <path d="M0 0 L460 0 L460 235 C 300 230, 140 200, 0 150 Z" fill="var(--swoosh)"/>
    </svg>
    <div class="lockup">
      <span class="lockup__dot"></span>
      <div class="lockup__text">
        <span class="lockup__name">The Hearth<br>Remedy</span>
        <span class="lockup__tagline">wholesome food choices for lasting everyday wellness</span>
      </div>
    </div>
    <span class="card__divider"></span>
    <h1 class="contact contact__heading">Name</h1>
    <p class="contact contact__role">Chef Dale Morrow<br>natural organic<br>and health supportive cooking</p>
    <p class="contact contact__details">Phone 305-617-4289<br>email dalemorrow@quillpost.example<br>web www.thehearthremedy.example</p>
    <span class="card__band"></span>
  </section>

</body>
</html>
```